SANDSTONE TRAIL TOURS Eye-catching design for A-frame sign (tour company Lightning Ridge - Australia)

We would need a simple but eye-catching design for our A-frame sign. The size of the sign is 595mm x 895mm. These signs stand on the curbside/outside various reception areas of motels and caravan parks here in Lightning Ridge. The aim is to make people book one of our tours. We have a design from previous years but there is too much info/words on there and it is hard to read. So we would like the new sign to be (quite) different. The base color should be black or dark. We don’t think we want big pictures on the sign but possibly the opal picture can somehow be integrated. This is only a though and not a must and we also are open to suggestion. The background can be one or more colors - solid or possibly different shades of it!?

I will attach an image of our current sign and of the sign of our competitor "Red Gum Excursions". We really like their sign and I have attached an image of it. Another image shows how the sign situation currently is. There are some places where only our signs is there but at most places it is in line with others.

We are a small family owned and operated tour operator in the outback of Australia. We are famous for precious black opals (just in case you don’t know but they are not black but very bright and colorful on the facing side:-). This is why most tourists come to Lightning Ridge to see our multi-cultural community, the opal mines and our very rare, precious and world-famous black opal.
Thanks a lot in advance for your interest and for your time to do a design for us here Down Under:-)

Target Market(s)

Grey nomads (pensioner), Families and young couples (oversea travellers)

Industry/Entity Type

Tourism

Font styles to use
Sans Serif

Colors

Designer to choose colors to be used in the design.

Requirements
Must have
• Our logo and the following info attached on word document.
Nice to have
• Please see description for this:-)
Should not have
• -Too small print
• -too crowded

```html
<!DOCTYPE html>
<html lang="en">
<head>
<meta charset="utf-8">
<title>Sandstone Trail Tours – A-frame sign</title>
<link rel="stylesheet" href="https://fonts.googleapis.com/css2?family=Bebas+Neue&family=Merriweather:ital,wght@1,700&family=Montserrat:wght@500;700;800&display=swap">
<style>
  :root {
    --page: #6b6b6b;
    --sign: #050505;
    --yellow: #fcd22a;
    --white: #ffffff;
    --coral: #ea5a6a;
    --orange: #f08a3c;
    --purple: #6e3f9c;
    --teal: #8fd6cc;
    --pink-band: #db4766;
    --frame-purple: #7b4ab0;
    --frame-pink: #d9456b;
  }
  * { margin: 0; padding: 0; box-sizing: border-box; }
  html, body { width: 1200px; height: 2861px; overflow: hidden; }
  body { background: var(--page); font-family: "Montserrat", sans-serif; position: relative; }

  .sign {
    position: absolute; left: 50px; top: 687px;
    width: 1100px; height: 1486px;
    background: radial-gradient(ellipse at 60% 55%, #141212 0%, var(--sign) 70%);
    box-shadow: 0 20px 40px rgba(0,0,0,.45);
    overflow: hidden;
  }

  .brand { position: absolute; left: 98px; top: 84px; display: flex; align-items: center; gap: 42px; }
  .brand-dot { width: 220px; height: 220px; border-radius: 50%; background: var(--yellow); flex: none; }
  .brand-text { color: var(--yellow); font-weight: 800; line-height: 1; }
  .brand-name { font-size: 68px; letter-spacing: 0.5px; }
  .brand-name + .brand-name { font-size: 60px; margin-top: 6px; }
  .brand-place { font-weight: 500; font-size: 50px; margin-top: 14px; padding-top: 12px; border-top: 3px solid var(--white); letter-spacing: 0.5px; }

  .headline { position: absolute; left: 0; width: 100%; top: 395px; text-align: center; font-family: "Bebas Neue", sans-serif; line-height: 1; }
  .headline-top { color: var(--white); font-size: 98px; letter-spacing: 0.5px; }
  .headline-bottom {
    font-size: 98px; letter-spacing: 12px; margin-top: 0px;
    background: linear-gradient(90deg, var(--coral), var(--orange));
    -webkit-background-clip: text; background-clip: text; color: transparent;
  }

  .tour-list { position: absolute; left: 122px; top: 599px; width: 756px; }
  .tour {
    position: relative; height: 129px; display: flex; align-items: center;
    border: 3px solid; border-image: linear-gradient(90deg, var(--frame-purple), var(--yellow) 55%, var(--frame-pink)) 1;
    margin-top: -3px;
  }
  .tour-dot { position: absolute; left: 54px; top: 42px; width: 44px; height: 44px; border-radius: 50%; background: var(--yellow); }
  .tour-divider { position: absolute; left: 142px; top: 36px; width: 3px; height: 56px; background: linear-gradient(var(--yellow), var(--frame-purple)); }
  .tour-text { margin-left: 178px; color: var(--white); font-weight: 500; font-size: 39px; line-height: 1.15; }
  .tour-text strong { color: var(--yellow); font-weight: 700; }

  .tagline { position: absolute; left: 0; width: 100%; top: 1030px; text-align: center; font-family: "Merriweather", serif; font-style: italic; font-weight: 700; font-size: 66px; color: var(--teal); }

  .phone-frame { position: absolute; left: 100px; top: 1215px; width: 800px; height: 130px; }
  .phone-number { position: absolute; left: 262px; top: 1225px; font-weight: 800; font-size: 94px; color: var(--yellow); line-height: 1.1; letter-spacing: 1px; }
  .phone-icon { position: absolute; left: 168px; top: 1246px; width: 70px; height: 70px; }
  .book-now {
    position: absolute; left: 306px; top: 1170px; width: 423px; height: 70px;
    background: var(--purple); border: 3px solid var(--yellow); border-radius: 35px;
    color: var(--white); font-weight: 800; font-size: 50px; text-align: center; line-height: 64px;
  }

  .web-band { position: absolute; left: 0; top: 1393px; width: 100%; height: 70px; background: var(--pink-band); color: var(--white); text-align: center; font-weight: 500; font-size: 31px; letter-spacing: 5px; line-height: 70px; }
  .web-band strong { font-weight: 700; }
</style>
</head>
<body>
  <main class="sign">
    <header class="brand">
      <div class="brand-dot"></div>
      <div class="brand-text">
        <div class="brand-name">SANDSTONE</div>
        <div class="brand-name">TRAIL TOURS</div>
        <div class="brand-place">LIGHTNING RIDGE</div>
      </div>
    </header>

    <h1 class="headline">
      <div class="headline-top">REAL TOURS BY LOCALS FOR</div>
      <div class="headline-bottom">THE REAL EXPERIENCE</div>
    </h1>

    <section class="tour-list">
      <div class="tour">
        <span class="tour-dot"></span><span class="tour-divider"></span>
        <p class="tour-text">The Ridge <strong>TOWN TOUR</strong><br>Daily 9am &amp; 2pm</p>
      </div>
      <div class="tour">
        <span class="tour-dot"></span><span class="tour-divider"></span>
        <p class="tour-text">Opal Fields &amp; Bush Pubs<br><strong>FULL DAY TOUR</strong></p>
      </div>
      <div class="tour">
        <span class="tour-dot"></span><span class="tour-divider"></span>
        <p class="tour-text"><strong>EVENING TOUR,</strong><br>Group &amp; Private Tours</p>
      </div>
    </section>

    <p class="tagline">You’ll Be Glad You Did</p>

    <svg class="phone-frame" viewBox="0 0 800 130" aria-hidden="true">
      <defs>
        <linearGradient id="frameStroke" x1="0" x2="1">
          <stop offset="0" stop-color="#d9456b"/>
          <stop offset="0.5" stop-color="#fcd22a"/>
          <stop offset="1" stop-color="#7b4ab0"/>
        </linearGradient>
      </defs>
      <polygon points="22,2 798,2 776,128 2,128" fill="none" stroke="url(#frameStroke)" stroke-width="3"/>
    </svg>
    <svg class="phone-icon" viewBox="0 0 70 70" aria-hidden="true">
      <circle cx="35" cy="35" r="32" fill="none" stroke="#7b4ab0" stroke-width="4"/>
      <path d="M24 18c3-2 5-1 7 3l3 6c1 2 0 4-2 5l-2 2c2 5 5 8 9 10l2-2c1-2 3-3 5-2l6 3c3 2 4 4 2 7-3 4-7 5-12 3-10-4-17-12-20-22-1-5 0-10 2-13z" fill="#7b4ab0"/>
    </svg>
    <div class="phone-number">02 5550 1234</div>
    <div class="book-now">BOOK NOW</div>

    <footer class="web-band">www.<strong>SandstoneTrailTours</strong>.com.au</footer>
  </main>
</body>
</html>
```